Customizable Form Generation Website

This will be a place for users to quickly generate numerous forms from a categorized list. As the forms are templates with field variables, the site must be able to substitute ‘real data’ for template variable data. This tool will allow for quick custom forms on-demand.

The landing page is attached. We need the User Experience and User Interface solved for us.

EXAMPLE:
——————————————————————-
Dear {{PatientFirstName}},

Please come back for an examination on {{SelectedDate}} with Doctor {{SelectedProvider}}.

Sincerely,

{{SelectedAuthor}}
——————————————————————-

Coming to the Forms Landing Page, the user will see the forms available to select. The user will then click to select a form.

At some point, the user must resolve the variables in the form. For instance, there are the following variables in the above example: PatientFirstName, SelectedDate, SelectedProvider, and SelectedAuthor. We must give the user a chance to select the values for these variables. Using a dropdown combobox will probably work for most. Getting a date selector will be required if the variable happens to contain the string 'date'.

Is it best to preselect common variables before opening the form, or is it best to dynamically scan the template, then give the user the option to give values to each variable found?

The design must include a way for users to upload additional forms. Forms will most probably be PDF, .DOC, .TXT files. This allows users to develop simple or fancy forms of their choosing., then simply drop them into the site for future use.

The design must include a way for users to create new forms. The form creation tool must present to the user the list of predefined variables like {{PatientLastName}} for easy insertion into the form writer. Anytime "{{}}" are used, developers will recognize that as a variable that needs to be resolved.

The forms will be separated into categories as follows:

OFFICE:
- Letterhead
- Sign-In Sheet
- Fax Cover Sheet
SCHEDULER:
- Appointment Reminder
- Missed Appointment Policy
PATIENT:
- Intake Form
- Patient Discharge
- Return to Work or School
- Excuse Slip
- Consent to Treat a Minor
- Verify Non-Pregnancy
RELEASE:
- Health Information Release Form
- X-Ray Release Form
CERTIFICATES:
- Certificate of Care
- Disability Certificate
INSURANCE:
- Authorization to Bill Insurance
- Assignment Authorization
OTHER:
- Free Massage
- Free Vitamins

The design must include a way to add/customize categories. Categories are for organizing the forms logically.

We welcome ANY questions to help understand the requirements.

Good luck!

Industry/Entity Type

Healthcare

Number of Pages Required

3 page

Requirements
Must have
• Must Follow ORBITAL SCHEMA standards
Nice to have
• Great User Experience. Simple, Fast, Clever.
Should not have
• nothing to add here

```html
<!DOCTYPE html>
<html lang="en">
<head>
<meta charset="utf-8">
<title>Forms App – Screens</title>
<link href="https://fonts.googleapis.com/css2?family=Montserrat:wght@500;600;700&family=Source+Sans+3:wght@400&display=swap" rel="stylesheet">
<style>
:root{
  --board:#a9aaae;
  --navy:#2f3e50;
  --slate:#53667b;
  --orange:#f15a24;
  --white:#ffffff;
  --paper:#f5f3f4;
  --ink:#1f2a36;
  --line:#c9ccd1;
  --avatar:#9aa3ad;
}
*{box-sizing:border-box;margin:0;padding:0}
html,body{width:1091px;height:1200px;overflow:hidden;background:var(--board);font-family:"Montserrat",sans-serif}
.screen{position:absolute;left:75px;width:958px;background:var(--white)}
.screen--form{top:85px;height:415px}
.screen--catalog{top:579px;height:523px;background:var(--paper)}
.topbar{position:absolute;left:0;top:0;width:100%;background:var(--navy)}
.screen--form .topbar{height:58px}
.screen--catalog .topbar{height:68px}
.brand{position:absolute;left:104px;color:var(--white);font-weight:600;font-size:20px;letter-spacing:.2px}
.header-btn{position:absolute;height:30px;border:1px solid var(--white);color:var(--white);font-weight:700;font-size:8.6px;display:flex;align-items:center;justify-content:center;letter-spacing:.2px;white-space:nowrap}
.create-btn{left:371px;width:110px}
.upload-btn{left:491px;width:164px}
.avatar{position:absolute;width:26px;height:26px;border-radius:50%;background:radial-gradient(circle at 50% 40%,#c9b9ae,var(--avatar))}
.welcome{position:absolute;color:var(--white);line-height:1.1}
.welcome small{display:block;font-size:9.5px;font-weight:500}
.welcome strong{display:block;font-size:11.5px;font-weight:700}
.logout-btn{position:absolute;left:790px;width:64px;height:25px;background:var(--orange);color:var(--white);font-weight:700;font-size:9.5px;display:flex;align-items:center;justify-content:center}
.greeting{position:absolute;left:105px;top:126px;font-size:13px;font-weight:700;color:var(--ink)}
.select{position:absolute;top:160px;width:240px;height:43px;border:1px solid var(--line);background:var(--white);padding:0 14px;display:flex;align-items:center;justify-content:space-between;font-size:10.5px;font-weight:500;color:var(--ink)}
.submit-btn{position:absolute;left:106px;top:221px;width:90px;height:35px;background:var(--orange);color:var(--white);font-weight:700;font-size:11.5px;display:flex;align-items:center;justify-content:center}
.footer{position:absolute;left:0;bottom:0;width:100%;background:var(--navy);color:var(--white);font-family:"Source Sans 3",sans-serif;font-size:10px;display:flex;align-items:center;justify-content:center}
.screen--form .footer{height:63px}
.screen--catalog .footer{height:60px}
.category-nav{position:absolute;left:0;top:68px;width:100%;height:41px;background:var(--slate)}
.category-list{position:absolute;left:105px;width:749px;top:0;height:41px;display:flex;align-items:center;justify-content:space-between}
.category{height:41px;display:flex;align-items:center;gap:7px;color:var(--white);font-weight:600;font-size:10px;white-space:nowrap}
.category--active{background:var(--navy);padding:0 11px}
.category svg{width:17px;height:17px;fill:none;stroke:var(--white);stroke-width:1.3;flex:none}
.manage-categories{width:24px;height:24px;border:1px solid var(--white);display:flex;align-items:center;justify-content:center}
.manage-categories svg{width:12px;height:12px;fill:none;stroke:var(--white);stroke-width:1.8}
.form-card{position:absolute;top:204px;width:238px;height:147px;background:var(--white);box-shadow:0 1px 3px rgba(0,0,0,.08);text-align:center}
.form-card svg{position:absolute;left:50%;top:28px;transform:translateX(-50%);width:52px;height:52px;fill:none;stroke:var(--orange);stroke-width:2.4}
.form-card span{position:absolute;left:0;right:0;top:98px;font-size:12.5px;font-weight:600;color:var(--navy)}
</style>
</head>
<body>

<section class="screen screen--form">
  <header class="topbar">
    <div class="brand" style="top:15px">Forms App</div>
    <div class="header-btn create-btn" style="top:14px">CREATE NEW FORM</div>
    <div class="header-btn upload-btn" style="top:14px">UPLOAD ADDITIONAL FORMS</div>
    <div class="avatar" style="left:677px;top:16px" role="img" aria-label="User profile photo"></div>
    <div class="welcome" style="left:713px;top:17px"><small>Welcome!</small><strong>DANIEL</strong></div>
    <div class="logout-btn" style="top:17px">LOGOUT</div>
  </header>
  <h1 class="greeting">Dear Daniel</h1>
  <div class="select" style="left:105px">Selected Date<svg width="10" height="6" viewBox="0 0 10 6"><path d="M1 1l4 4 4-4" fill="none" stroke="#1f2a36" stroke-width="1.3"/></svg></div>
  <div class="select" style="left:359px">SelectedProvider<svg width="10" height="6" viewBox="0 0 10 6"><path d="M1 1l4 4 4-4" fill="none" stroke="#1f2a36" stroke-width="1.3"/></svg></div>
  <div class="select" style="left:613px">Selected Author<svg width="10" height="6" viewBox="0 0 10 6"><path d="M1 1l4 4 4-4" fill="none" stroke="#1f2a36" stroke-width="1.3"/></svg></div>
  <div class="submit-btn">SUBMIT</div>
  <footer class="footer">Copyright © 2021 All Rights Reserved</footer>
</section>

<section class="screen screen--catalog">
  <header class="topbar">
    <div class="brand" style="top:20px">Forms App</div>
    <div class="header-btn create-btn" style="top:19px">CREATE NEW FORM</div>
    <div class="header-btn upload-btn" style="top:19px">UPLOAD ADDITIONAL FORMS</div>
    <div class="avatar" style="left:674px;top:21px" role="img" aria-label="User profile photo"></div>
    <div class="welcome" style="left:710px;top:22px"><small>Welcome!</small><strong>DANIEL</strong></div>
    <div class="logout-btn" style="top:21px">LOGOUT</div>
  </header>
  <nav class="category-nav">
    <div class="category-list">
      <div class="category category--active">
        <svg viewBox="0 0 20 20"><path d="M2 19h16M4 19V9h4v10M8 19V2h8v17M10 5h1M13 5h1M10 8h1M13 8h1M10 11h1M13 11h1M10 14h1M13 14h1M5 12h1M5 15h1"/></svg>OFFICE</div>
      <div class="category">
        <svg viewBox="0 0 20 20"><path d="M2 4h16v14H2zM2 8h16M6 2v4M14 2v4M6 11h2M10 11h2M14 11h1M6 14h2M10 14h2"/></svg>SCHEDULER</div>
      <div class="category">
        <svg viewBox="0 0 20 20"><circle cx="10" cy="6" r="4"/><path d="M3 19c0-4 3-6 7-6s7 2 7 6z"/></svg>PATIENT</div>
      <div class="category">
        <svg viewBox="0 0 20 20"><path d="M8 12l-3-3 4-4c3-3 7-4 9-3 1 2 0 6-3 9l-4 4z"/><circle cx="13" cy="7" r="1.5"/><path d="M6 14l-4 4M5 11l-3 3M9 15l-3 3"/></svg>RELEASE</div>
      <div class="category">
        <svg viewBox="0 0 20 20"><path d="M4 2h12v16H4zM7 6h6M7 9h6M7 12h3"/><circle cx="13" cy="14" r="2"/></svg>CERTIFICATES</div>
      <div class="category">
        <svg viewBox="0 0 20 20"><path d="M10 18H3V2h11v7M6 6h5M6 9h5M6 12h2"/><path d="M15 11l4 1.5v2.5c0 2-2 3.5-4 4-2-.5-4-2-4-4v-2.5z"/><path d="M13.5 15l1 1 2-2"/></svg>INSURANCE</div>
      <div class="category">
        <svg viewBox="0 0 20 20" style="stroke-width:2"><path d="M3 5h14M3 10h14M3 15h14"/></svg>OTHER</div>
      <div class="manage-categories" role="button" aria-label="Add or customise categories" title="Manage categories">
        <svg viewBox="0 0 12 12"><path d="M6 1v10M1 6h10"/></svg></div>
    </div>
  </nav>

  <div class="form-card" style="left:106px">
    <svg viewBox="0 0 52 52"><path d="M8 3h36v46H8z"/><path d="M17 12h10v10H17zM17 31h18M17 38h18"/></svg>
    <span>LETTERHEAD</span>
  </div>
  <div class="form-card" style="left:360px">
    <svg viewBox="0 0 52 52"><path d="M22 10H33V22M33 36V44H22"/><path d="M4 10l18-6v44L4 42z"/><path d="M50 26H28M35 19l-7 7 7 7"/></svg>
    <span>SIGN-IN SHEET</span>
  </div>
  <div class="form-card" style="left:614px">
    <svg viewBox="0 0 52 52"><path d="M13 16V4h26v12"/><path d="M13 38H6V18c0-1 1-2 2-2h36c1 0 2 1 2 2v20h-7"/><path d="M13 30h26v18H13zM19 37h14M19 42h10"/><path d="M39 22h3"/></svg>
    <span>FAX COVER SHEET</span>
  </div>

  <footer class="footer">Copyright © 2021 All Rights Reserved</footer>
</section>

</body>
</html>
```